Facebook Post for Fence Spring Sale

We have a $12 / FT Fence sale that we have been running for a while now. We need a flyer made up for SPRING.

Our previous flyer can be seen here:
https://media.pixvault-host.example/img/48213907_551903288146720_7391026458813302947_n.jpg?ref=7c21b9e04d8a

We want to use the photos that are shown here https://files.cloudtrove-share.example/view?id=9XkQ7rTmw2LpZdVa4HsE in the flyer. This is to be posted on Facebook so it must be the proper size for Facebook page post.

The wording to be used should be "Spring Fence Sale" and "$12 / FT Wood Fences" Also we should include our business name "Oakridge Fence" and phone number for Free Estimates - 555-314-2076.

Residential Construction

Font styles to use
Serif
Sans Serif

Colors
3176b5
fbee3d
fbed22
fbf289
85cae6
33a6d7

Requirements
Must have
• Phone number, $12 / FT Fence Sale

```html
<!DOCTYPE html>
<html lang="en">
<head>
<meta charset="utf-8">
<title>Oakridge Fence – Spring Fence Sale</title>
<link rel="stylesheet" href="https://fonts.googleapis.com/css2?family=Montserrat:wght@300;400;500;700;800&display=swap">
<style>
  :root {
    --blue: #3176b5;
    --sky: #33a6d7;
    --pale-blue: #85cae6;
    --yellow: #fbee3d;
    --yellow-deep: #fbed22;
    --yellow-soft: #fbf289;
    --backdrop: #dcdcde;
  }
  * { margin: 0; padding: 0; box-sizing: border-box; }
  html, body {
    width: 1062px; height: 1200px; overflow: hidden;
    background: var(--backdrop);
  }
  .canvas {
    position: relative; width: 1062px; height: 1200px; overflow: hidden;
  }
  .flyer {
    position: absolute; left: 0; top: 69px;
    width: 960px; height: 960px;
    transform: scale(1.10625); transform-origin: 0 0;
    background: var(--yellow-deep);
    font-family: 'Montserrat', sans-serif;
    color: var(--blue);
  }
  .headline {
    position: absolute; left: 53px; top: 62px;
    font-size: 68px; font-weight: 800; letter-spacing: -0.5px; line-height: 1;
  }
  .sale-ribbon {
    position: absolute; left: 616px; top: 34px; width: 298px; height: 120px;
  }
  .sale-ribbon svg { position: absolute; inset: 0; }
  .sale-ribbon .sale-word {
    position: absolute; left: 30px; top: 28px;
    font-size: 66px; font-weight: 800; line-height: 1; color: var(--yellow);
  }
  .offer {
    position: absolute; left: 53px; top: 164px;
    font-size: 62px; font-weight: 300; letter-spacing: 6px; line-height: 1; white-space: nowrap;
  }
  .offer .price { font-weight: 800; letter-spacing: 1px; }
  .gallery {
    position: absolute; left: 0; top: 260px; width: 960px; height: 507px;
    background: var(--yellow-soft);
  }
  .photo { position: absolute; }
  .photo--arched { left: 0; top: 15px; width: 376px; height: 378px;
    background: linear-gradient(160deg, #e0bd7c, #c99a55 60%, #8a6a3c); }
  .photo--scalloped { left: 386px; top: 15px; width: 277px; height: 227px;
    background: linear-gradient(180deg, #8b7d70 0%, #d8b67a 35%, #b98c52); }
  .photo--picket { left: 673px; top: 15px; width: 287px; height: 227px;
    background: linear-gradient(180deg, #e6e4de 0%, #7fa04a 35%, #e3c995 70%, #8aa450); }
  .photo--privacy { left: 387px; top: 255px; width: 573px; height: 239px;
    background: linear-gradient(180deg, #eee9c4 0%, #ece6bc 68%, #4d6b2e 72%, #3e5a24); }
  .brand {
    position: absolute; left: 56px; top: 418px;
    display: flex; align-items: center; gap: 14px;
  }
  .brand .mark { width: 22px; height: 22px; border-radius: 50%; background: var(--blue); }
  .brand .name { font-size: 26px; font-weight: 700; color: var(--blue); }
  .tagline {
    position: absolute; left: 0; right: 0; top: 808px; text-align: center;
    font-size: 19px; font-weight: 500; letter-spacing: 7.2px;
  }
  .divider {
    position: absolute; left: 0; right: 0; top: 839px; height: 1px;
    background: var(--yellow-soft);
  }
  .estimate {
    position: absolute; left: 51px; top: 880px;
    font-size: 34px; font-weight: 400; color: var(--sky); line-height: 1; white-space: nowrap;
  }
  .estimate strong { font-weight: 700; }
  .estimate small { font-size: 24px; font-weight: 500; }
  .phone {
    position: absolute; left: 492px; top: 866px;
    font-size: 57px; font-weight: 800; color: var(--blue); line-height: 1; letter-spacing: -0.5px;
  }
</style>
</head>
<body>
<div class="canvas">
  <section class="flyer">
    <h1 class="headline">SPRING FENCE</h1>
    <div class="sale-ribbon">
      <svg viewBox="0 0 298 120" width="298" height="120" aria-hidden="true">
        <defs>
          <linearGradient id="ribbonFill" x1="0" y1="0" x2="1" y2="0">
            <stop offset="0" stop-color="#3176b5"/>
            <stop offset="0.65" stop-color="#33a6d7"/>
            <stop offset="1" stop-color="#85cae6"/>
          </linearGradient>
        </defs>
        <path d="M14 22 Q150 -2 296 4 L288 104 Q150 96 6 118 Z" fill="url(#ribbonFill)"/>
      </svg>
      <span class="sale-word">SALE</span>
    </div>
    <p class="offer"><span class="price">$12</span> / FT WOOD FENCES</p>

    <div class="gallery">
      <div class="photo photo--arched" role="img" aria-label="Photo of a tall wooden privacy fence with an arched top beside a brick house"></div>
      <div class="photo photo--scalloped" role="img" aria-label="Photo of a wooden privacy fence with a scalloped top along a backyard"></div>
      <div class="photo photo--picket" role="img" aria-label="Photo of a wooden picket fence running across a green lawn"></div>
      <div class="photo photo--privacy" role="img" aria-label="Photo of a long new flat-top wooden privacy fence above grass"></div>
      <div class="brand">
        <span class="mark"></span>
        <span class="name">Oakridge Fence</span>
      </div>
    </div>

    <p class="tagline">BECAUSE GOOD FENCES MAKE GOOD NEIGHBORS</p>
    <div class="divider"></div>
    <p class="estimate">For <strong>Free</strong> Estimates <small>call:</small></p>
    <p class="phone">555-314-2076</p>
  </section>
</div>
</body>
</html>
```